Real estate business needing a creative mind!

Have a real estate business called Brightlane Estates LLC. I need some business card with custom logo. That logo can be an intricate design of a house or houses. Maybe some blue and orange colors, maybe the business name in orange. Some thing that leaves a wow impression to the holder. Or just surprise me! Must have business name, name, email and phone number.

Target Market(s)

Property sellers and real estate professionals

Industry/Entity Type

Real estate

Contact Information for Business Card

Want it to stand out but also be professional.

Colors

Designer to choose colors to be used in the design.

Requirements
Must have
• Business name Brightlane Estates. My name which is Dale Venbrook. The business email which is Brightlaneestates1@mailpost.example. The phone number which is 555-604-1928
Nice to have
• Could be a logo of the name over some mountain houses being that we live by the Smokey mountains. Could have a sun if it looks ok?

```html
<!DOCTYPE html>
<html lang="en">
<head>
<meta charset="UTF-8">
<title>Brightlane Estates LLC — Business Card</title>
<link href="https://fonts.googleapis.com/css2?family=Montserrat:wght@700&family=Lato:wght@400;700&display=swap" rel="stylesheet">
<style>
  :root {
    --stage: #3a3a3a;
    --card: #ffffff;
    --orange: #ff6a13;
    --blue: #1a9ff0;
    --ink: #2b2b2b;
  }
  * { box-sizing: border-box; margin: 0; padding: 0; }
  html, body { width: 1200px; height: 875px; overflow: hidden; }
  body {
    background: var(--stage);
    position: relative;
    font-family: "Lato", sans-serif;
  }
  .card {
    position: absolute;
    width: 560px;
    height: 320px;
    background: var(--card);
    border-radius: 18px;
    box-shadow: 0 18px 40px rgba(0,0,0,0.45);
    overflow: hidden;
  }
  .card--front { left: 70px; top: 80px; }
  .card--back { right: 70px; top: 475px; }

  .wordmark {
    display: flex;
    align-items: center;
    gap: 12px;
    font-family: "Montserrat", sans-serif;
    font-weight: 700;
    color: var(--orange);
    text-transform: uppercase;
    line-height: 1;
    white-space: nowrap;
  }
  .wordmark__dot {
    width: 16px; height: 16px;
    border-radius: 50%;
    background: var(--orange);
    flex: none;
  }
  .card--front .wordmark {
    position: absolute;
    left: 50%; top: 50%;
    transform: translate(-50%, -50%);
    font-size: 27px;
    letter-spacing: 0.5px;
  }
  .card--back .wordmark {
    position: absolute;
    right: 34px; top: 34px;
    font-size: 18px;
    gap: 10px;
  }
  .card--back .wordmark__dot { width: 12px; height: 12px; }

  .rule {
    position: absolute;
    height: 3px;
    background: var(--blue);
  }
  .rule--top { left: 230px; right: 34px; top: 84px; }
  .rule--mid { left: 38px; width: 290px; top: 196px; }

  .agent {
    position: absolute;
    left: 38px; top: 128px;
  }
  .agent__name {
    font-family: "Montserrat", sans-serif;
    font-weight: 700;
    font-size: 34px;
    color: var(--blue);
    text-transform: uppercase;
    line-height: 1;
  }
  .agent__role {
    font-size: 17px;
    color: var(--orange);
    margin-top: 6px;
  }

  .contact {
    position: absolute;
    left: 42px; top: 212px;
    list-style: none;
    font-size: 15px;
    color: var(--ink);
  }
  .contact li {
    display: flex;
    align-items: center;
    gap: 10px;
    height: 28px;
  }
  .contact__phone { font-size: 18px; }
  .contact svg { width: 14px; height: 14px; flex: none; }
</style>
</head>
<body>
  <section class="card card--front">
    <div class="wordmark"><span class="wordmark__dot"></span>Brightlane Estates LLC</div>
  </section>

  <section class="card card--back">
    <div class="wordmark"><span class="wordmark__dot"></span>Brightlane Estates LLC</div>
    <div class="rule rule--top"></div>

    <div class="agent">
      <h1 class="agent__name">Dale Venbrook</h1>
      <p class="agent__role">Real Estate Agent</p>
    </div>
    <div class="rule rule--mid"></div>

    <ul class="contact">
      <li class="contact__phone">
        <svg viewBox="0 0 24 24" aria-hidden="true"><path fill="#ff6a13" d="M6.6 10.8a15 15 0 0 0 6.6 6.6l2.2-2.2a1 1 0 0 1 1-.25 11.4 11.4 0 0 0 3.6.57 1 1 0 0 1 1 1V20a1 1 0 0 1-1 1A17 17 0 0 1 3 4a1 1 0 0 1 1-1h3.5a1 1 0 0 1 1 1c0 1.25.2 2.45.57 3.6a1 1 0 0 1-.25 1z"/></svg>
        555-604-1928
      </li>
      <li>
        <svg viewBox="0 0 24 24" aria-hidden="true"><rect x="2" y="5" width="20" height="14" rx="1.5" fill="#ff6a13"/><path d="M3 6l9 7 9-7" fill="none" stroke="#fff" stroke-width="1.8"/></svg>
        Brightlaneestates1@mailpost.example
      </li>
      <li>
        <svg viewBox="0 0 24 24" aria-hidden="true"><circle cx="12" cy="12" r="9.5" fill="none" stroke="#ff6a13" stroke-width="2"/><path d="M2.5 12h19M12 2.5c3 3 3 16 0 19M12 2.5c-3 3-3 16 0 19" fill="none" stroke="#ff6a13" stroke-width="1.6"/></svg>
        brightlaneestatesllc.example
      </li>
    </ul>
  </section>
</body>
</html>
```